Kestrel Homes Web Site Design

improve on the graphic design on our current website
www.kestrelhmoes.com.au
wordpress required

Industry/Entity Type

Graphic Design

Coding

Coded - Design and coding required

Number of Pages Required

5+ page

```html
<!DOCTYPE html>
<html lang="en">
<head>
<meta charset="utf-8">
<title>Kestrel Homes – Canberra's Boutique Builders</title>
<link rel="stylesheet" href="https://fonts.googleapis.com/css2?family=Roboto:wght@300;400;500;700&family=Roboto+Slab:wght@300;700&display=swap">
<style>
:root{
  --red:#c11f2e;
  --red-bright:#e0202f;
  --bar:#2b2828;
  --ink:#333;
  --grey:#6a6a6a;
  --white:#fff;
  --band:rgba(38,34,34,.78);
  --feature-text:#cfcfcf;
}
*{margin:0;padding:0;box-sizing:border-box}
html,body{width:1200px;height:703px;overflow:hidden;background:var(--white);font-family:'Roboto',sans-serif;color:var(--ink)}
.page{position:relative;width:1200px;height:703px}

/* top bar */
.topbar{position:absolute;left:0;top:0;width:1200px;height:42px;background:var(--bar);color:#cfcfcf;font-size:12.5px;white-space:nowrap}
.topbar .hours{position:absolute;left:170px;top:14px}
.topbar .quote{position:absolute;left:469px;top:11px;display:flex;align-items:center;gap:6px}
.topbar .quote a{color:var(--red-bright);font-weight:700;font-size:17px;line-height:20px;text-decoration:none;font-family:'Roboto Slab',serif}
.topbar .call{position:absolute;left:751px;top:11px;display:flex;align-items:center;gap:6px}
.topbar .call strong{color:var(--red-bright);font-size:17px;line-height:20px;font-weight:700}
.topbar .divider{position:absolute;left:963px;top:15px;width:1px;height:13px;background:#777}
.topbar .cart{position:absolute;left:976px;top:12px;display:flex;align-items:center;gap:6px;font-size:13.5px}

/* header */
.header{position:absolute;left:0;top:42px;width:1200px;height:83px;background:var(--white)}
.brand{position:absolute;left:170px;top:23px;display:flex;align-items:center;gap:10px;font-weight:500;font-size:25px;line-height:36px;color:var(--grey);white-space:nowrap}
.brand .mark{width:36px;height:36px;border-radius:50%;background:var(--red)}
.nav a{position:absolute;top:27px;height:32px;line-height:32px;font-size:15px;color:#3a3a3a;text-decoration:none;white-space:nowrap}
.nav a.active{left:499px;width:70px;text-align:center;border-radius:16px;background:var(--red);color:var(--white)}
.search{position:absolute;left:1003px;top:26px;width:34px;height:33px;border:1px solid #ccc;display:flex;align-items:center;justify-content:center}

/* hero */
.hero{position:absolute;left:0;top:125px;width:1200px;height:532px}
.hero-photo{position:absolute;inset:0;background:
  linear-gradient(90deg,rgba(0,0,0,.18),rgba(0,0,0,0) 30%),
  linear-gradient(180deg,#5e5a5c 0%,#7d787a 35%,#6a5b5c 60%,#3b2b2c 85%,#2a2222 100%)}
.hero-photo::after{content:"";position:absolute;left:672px;top:0;width:528px;height:428px;background:linear-gradient(180deg,#b7b1b3,#d6d0d1 60%,#8f8a8b)}
.hero-title{position:absolute;left:170px;top:160px;font-family:'Roboto Slab',serif;font-weight:300;font-size:39px;line-height:46px;color:var(--white);text-shadow:1px 2px 4px rgba(0,0,0,.45);white-space:nowrap}
.hero-title b{font-weight:700}
.cta{position:absolute;left:170px;top:270px;width:185px;height:41px;border-radius:21px;background:var(--red);color:var(--white);font-size:16.5px;display:flex;align-items:center;justify-content:center;text-decoration:none}
.arrow-left{position:absolute;left:12px;top:200px}
.arrow-right{position:absolute;left:1153px;top:167px;width:100px;height:100px;border-radius:50%;background:rgba(255,255,255,.15)}
.arrow-right svg{position:absolute;left:20px;top:34px}

/* feature band */
.features{position:absolute;left:0;top:428px;width:1200px;height:104px;background:var(--band)}
.feature{position:absolute;top:0;height:104px;display:flex;align-items:center;gap:17px;color:var(--feature-text);font-size:17.5px;font-weight:300;line-height:21px;white-space:nowrap}
.feature .icon{width:58px;height:58px;border-radius:50%;background:#1a1616;display:flex;align-items:center;justify-content:center}
.feature-split{position:absolute;top:0;height:104px;border-left:1px dashed rgba(255,255,255,.3)}

/* footer */
.footer{position:absolute;left:0;top:657px;width:1200px;height:46px;font-size:12px;color:#3a3a3a}
.footer .copy{position:absolute;left:170px;top:17px}
.footer .social{position:absolute;right:164px;top:12px;display:flex;align-items:center;gap:5px}
.footer .social span.label{margin-right:4px}
.footer .dot{width:21px;height:21px;border-radius:50%;background:#222}
.footer .dot.alt{background:var(--red)}
</style>
</head>
<body>
<div class="page">
  <div class="topbar">
    <span class="hours">Mon – Fri: 7.00 – 19.00 · Sat - Sun: 9.00 - 15.00</span>
    <span class="quote">
      <svg width="15" height="11" viewBox="0 0 15 11"><rect x=".5" y=".5" width="14" height="10" fill="#999"/><path d="M.5 .5 7.5 6 14.5 .5" stroke="#2b2828" fill="none"/></svg>
      Need an Estimate? <a href="#">GET A QUOTE &gt;</a>
    </span>
    <span class="call">
      <svg width="9" height="15" viewBox="0 0 9 15"><rect x=".5" y=".5" width="8" height="14" rx="1.5" fill="none" stroke="#999"/><rect x="2" y="2" width="5" height="9" fill="#999"/></svg>
      Call Us Now: <strong>0400 318 762</strong>
    </span>
    <span class="divider"></span>
    <span class="cart">
      <svg width="17" height="14" viewBox="0 0 17 14"><path d="M1 4h15l-2 9H3z" fill="#bbb"/><path d="M5 4 8 0M12 4 9 0" stroke="#bbb" fill="none"/></svg>
      0 Item
    </span>
  </div>

  <header class="header">
    <div class="brand"><span class="mark"></span>Kestrel Homes</div>
    <nav class="nav">
      <a class="active" href="#">Home</a>
      <a href="#" style="left:579px">Company</a>
      <a href="#" style="left:663px">Excellence</a>
      <a href="#" style="left:755px">Experience</a>
      <a href="#" style="left:849px">Expertise</a>
      <a href="#" style="left:932px">Contact</a>
    </nav>
    <div class="search">
      <svg width="18" height="18" viewBox="0 0 18 18"><circle cx="7" cy="7" r="5" fill="none" stroke="#777" stroke-width="2"/><path d="M11 11 16 16" stroke="#777" stroke-width="3"/></svg>
    </div>
  </header>

  <section class="hero">
    <div class="hero-photo" role="img" aria-label="Modern living room with red leather sofas, framed art and red wall shelving"></div>
    <h1 class="hero-title"><b>WELCOME</b> TO<br>CANBERRA’S BOUTIQUE BUILDERS</h1>
    <a class="cta" href="#">See Our Portfolio &gt;</a>
    <svg class="arrow-left" width="16" height="30" viewBox="0 0 16 30"><path d="M14 1 2 15 14 29" stroke="#ddd" stroke-width="2" fill="none"/></svg>
    <div class="arrow-right"><svg width="16" height="30" viewBox="0 0 16 30"><path d="M2 1 14 15 2 29" stroke="#eee" stroke-width="2" fill="none"/></svg></div>

    <div class="features">
      <div class="feature" style="left:227px">
        <span class="icon"><svg width="32" height="30" viewBox="0 0 32 30" fill="none" stroke="#c11f2e" stroke-width="2"><rect x="3" y="10" width="9" height="18"/><rect x="12" y="3" width="10" height="25"/><rect x="22" y="12" width="7" height="16"/><path d="M15 8h4M15 13h4M15 18h4M6 15h3M6 20h3M24 17h3M24 22h3"/></svg></span>
        <span>Canberra<br>Building Services</span>
      </div>
      <div class="feature-split" style="left:482px"></div>
      <div class="feature" style="left:538px">
        <span class="icon"><svg width="28" height="32" viewBox="0 0 28 32" fill="none" stroke="#c11f2e" stroke-width="2"><circle cx="14" cy="5" r="3"/><path d="M12 8 4 30M16 8l8 22M7 21q7 4 14 0"/></svg></span>
        <span>Top Class<br>Architects</span>
      </div>
      <div class="feature-split" style="left:748px"></div>
      <div class="feature" style="left:812px">
        <span class="icon"><svg width="36" height="26" viewBox="0 0 36 26" fill="#c11f2e"><rect x="2" y="11" width="18" height="8"/><rect x="5" y="5" width="9" height="6"/><path d="M18 11 27 2l6 8-2 2-5-5-6 6z"/><rect x="1" y="20" width="22" height="4" rx="2"/></svg></span>
        <span>Reliable<br>Contractors</span>
      </div>
    </div>
  </section>

  <footer class="footer">
    <span class="copy">© 2016 Kestrel Home Builders Canberra</span>
    <div class="social">
      <span class="label">Stay connected:</span>
      <span class="dot" aria-label="Social link 1"></span>
      <span class="dot alt" aria-label="Social link 2"></span>
      <span class="dot" aria-label="Social link 3"></span>
    </div>
  </footer>
</div>
</body>
</html>
```